Marlow Fields Thank-You Tag

Looking for a file that incorporates current branding/colors and says:

"Thanks for Swimming with Us!"
Marlow Fields Otters

Samples of other pieces we've done recently are attached.

Will be printed on cardstock that is
Width: 3.5 inches
Height: 2.5 inches

```html
<!DOCTYPE html>
<html lang="en">
<head>
<meta charset="utf-8">
<title>Marlow Fields Thank-You Tag</title>
<link rel="stylesheet" href="https://fonts.googleapis.com/css2?family=Anton&family=Roboto+Condensed:wght@700&display=swap">
<style>
  :root {
    --navy: #354785;
    --navy-deep: #2e3c76;
    --wave-mid: #43558f;
    --sky: #98bade;
    --pink: #e05d8a;
    --white: #ffffff;
    --paper: #ffffff;
  }
  * { margin: 0; padding: 0; box-sizing: border-box; }
  html, body {
    width: 936px; height: 1200px; overflow: hidden; background: var(--paper);
  }
  .canvas { position: relative; width: 936px; height: 1200px; }
  .tag {
    position: absolute; left: 157px; top: 160px; width: 611px; height: 856px;
    background: var(--navy); overflow: hidden;
  }
  .tag-art { position: absolute; inset: 0; width: 611px; height: 856px; }
  .headline {
    position: absolute; left: 0; top: 66px; width: 100%;
    text-align: center; color: var(--sky);
    font-family: "Anton", sans-serif; font-size: 150px; line-height: 1;
    letter-spacing: 4px; transform: scaleX(1.12);
  }
  .subline {
    position: absolute; left: 0; top: 248px; width: 100%;
    text-align: center; color: var(--white);
    font-family: "Roboto Condensed", sans-serif; font-weight: 700;
    font-size: 54px; line-height: 60px; letter-spacing: 1px;
  }
  .club-name {
    position: absolute; left: 196px; top: 500px; width: 220px;
    text-align: center; color: var(--white);
    font-family: "Roboto Condensed", sans-serif; font-weight: 700;
    font-size: 34px; line-height: 38px; letter-spacing: 2px;
  }
</style>
</head>
<body>
<div class="canvas">
  <div class="tag">
    <svg class="tag-art" viewBox="0 0 611 856" xmlns="http://www.w3.org/2000/svg">
      <rect class="leaping-illustration" x="30" y="369" width="210" height="190" rx="60" fill="var(--navy-deep)" opacity="0.55" role="img" aria-label="Leaping figure with water splashes, left side"/>
      <rect class="leaping-illustration" x="400" y="369" width="190" height="190" rx="60" fill="var(--navy-deep)" opacity="0.55" role="img" aria-label="Leaping figure with water splashes, right side"/>
      <path class="wave wave-mid" d="M0 560 C120 545 220 640 306 690 C380 650 480 575 611 580 V856 H0Z" fill="var(--wave-mid)"/>
      <path class="wave wave-white" d="M0 626 C120 620 200 700 300 716 C420 730 500 640 611 636 V856 H0Z" fill="var(--white)"/>
      <path class="wave wave-sky" d="M0 642 C120 636 200 716 300 732 C420 746 500 660 611 654 V856 H0Z" fill="var(--sky)"/>
      <path class="wave wave-white" d="M0 703 C130 690 250 780 350 787 C450 794 520 716 611 716 V856 H0Z" fill="var(--white)"/>
      <path class="wave wave-pink" d="M0 728 C130 712 250 810 338 820 C440 830 520 740 611 742 V856 H0Z" fill="var(--pink)"/>
      <circle class="club-badge" cx="306" cy="555" r="127" fill="var(--navy)" stroke="var(--pink)" stroke-width="20"/>
    </svg>
    <div class="headline">THANKS</div>
    <div class="subline">FOR SWIMMING<br>WITH US!</div>
    <div class="club-name">MARLOW FIELDS<br>OTTERS</div>
  </div>
</div>
</body>
</html>
```